Brenner & Holloway Stationery

Greetings again. Now we've got an awesome logo, it's time to get the stationery to go with it. We require the following items of stationery:

- Business Card - Print Ready, all we need to do is change names and numbers and submit to printer.  Double sided with logo on one side and details on the other side. (85mm x 55mm)

- With Compliments Slip

- Letterhead - These will be preprinted pages that will then be used as pages.
(A4)

- Envelope - Business Size(Standard DL)

Target Market(s)

Essentially, this firm services clients facing criminal charges and/or seeking legal aid. The firm is also looking at taking on more white-collar crime cases.

Requirements
Must have
• - Same Design Cues & Colours as the Branding details attached

• - Address (as follows)

• Suite 8

• 262-268 Marlow St

• KELVALE VIC 3190

• Phone: (03) 9482 6315

• Fax: (03) 9482 6840

• Web: www.brennerandholloway.example.au

• - Colour: Pantone 194 (Red)

```html
<!DOCTYPE html>
<html lang="en">
<head>
<meta charset="utf-8">
<title>Brenner &amp; Holloway — Business Card</title>
<link rel="stylesheet" href="https://fonts.googleapis.com/css2?family=Cinzel:wght@500&family=EB+Garamond:wght@400;700&display=swap">
<style>
  :root {
    --brand-red: #ac1f36;
    --ink: #1c1c1e;
    --frame-dark: #2f2f34;
    --paper: #ffffff;
    --paper-tint: #fdf8f8;
    --rule-grey: #b9b9bd;
  }
  * { margin: 0; padding: 0; box-sizing: border-box; }
  html, body {
    width: 945px;
    height: 1200px;
    overflow: hidden;
    background: var(--paper);
  }
  .sheet {
    position: relative;
    width: 945px;
    height: 1200px;
  }
  .card {
    position: absolute;
    left: 37px;
    width: 871px;
    height: 564px;
    overflow: hidden;
    box-shadow: 0 2px 8px rgba(0, 0, 0, 0.35);
  }
  .card--front { top: 24px; background: var(--brand-red); }
  .card--back  { top: 622px; background: var(--paper); }

  .card__pattern {
    position: absolute;
    inset: 0;
  }
  .card--front .card__pattern { background: var(--brand-red); }
  .card--back .card__pattern  { background: var(--paper-tint); }

  /* Front: logo tab */
  .logo-tab {
    position: absolute;
    left: 205px;
    top: 353px;
    width: 460px;
    height: 230px;
    background: var(--paper);
    border: 7px solid var(--frame-dark);
    border-bottom: none;
    border-radius: 38px 38px 0 0;
    box-shadow: 0 0 0 5px var(--paper);
  }
  .lockup {
    position: absolute;
    left: 38px;
    top: 60px;
    display: flex;
    align-items: center;
  }
  .lockup__mark {
    width: 92px;
    height: 92px;
    border-radius: 50%;
    background: var(--brand-red);
    flex: none;
  }
  .lockup__rule {
    width: 1px;
    height: 92px;
    background: var(--rule-grey);
    margin: 0 18px 0 18px;
  }
  .lockup__name {
    font-family: "Cinzel", serif;
    font-weight: 500;
    font-size: 23px;
    line-height: 1.0;
    color: var(--ink);
    letter-spacing: 0;
  }
  .lockup__tagline {
    display: block;
    font-size: 14.5px;
    letter-spacing: 0.08em;
    margin-top: 3px;
  }

  /* Back: details */
  .details {
    position: absolute;
    left: 0;
    right: 0;
    text-align: center;
    font-family: "EB Garamond", serif;
    color: var(--ink);
  }
  .details__name {
    top: 312px;
    font-weight: 700;
    font-size: 32px;
    letter-spacing: 0.2em;
    text-transform: uppercase;
    padding-left: 0.2em;
  }
  .details__role {
    top: 352px;
    font-size: 17px;
    letter-spacing: 0.3em;
    text-transform: uppercase;
    padding-left: 0.3em;
  }
  .details__contact {
    top: 432px;
    font-size: 17px;
    line-height: 26px;
    letter-spacing: 0.28em;
    text-transform: uppercase;
  }
  .details__contact .sep { margin: 0 0.7em; }
</style>
</head>
<body>
  <main class="sheet">
    <section class="card card--front">
      <div class="card__pattern" role="img" aria-label="Repeating tonal ornament pattern on brand red"></div>
      <div class="logo-tab">
        <div class="lockup">
          <span class="lockup__mark" aria-hidden="true"></span>
          <span class="lockup__rule" aria-hidden="true"></span>
          <p class="lockup__name">Brenner &amp; Holloway
            <span class="lockup__tagline">Barristers &amp; Solicitors</span>
          </p>
        </div>
      </div>
    </section>

    <section class="card card--back">
      <div class="card__pattern" role="img" aria-label="Faint repeating ornament pattern on white"></div>
      <h1 class="details details__name">Daniel Whitford</h1>
      <p class="details details__role">Managing Director</p>
      <p class="details details__contact">
        Suite 8<span class="sep">|</span>262-268 Marlow St<span class="sep">|</span>Kelvale VIC 3190<span class="sep">|</span><br>
        Phone: (03) 9482 6315<span class="sep">|</span>Fax: (03) 9482 6840<span class="sep">|</span><br>
        Web: www.brennerandholloway.example.au<span class="sep">|</span>
      </p>
    </section>
  </main>
</body>
</html>
```